Unique business card design

Boutique coastal hotel suites - in need of clever stand out business card I have uploaded the logo that I had created through quill forge I want something that is clever and stands out from everyone else - 418 Brantwell Avenue seldovia Alaska 99571 phone or text 907 -581-6142 www.primemarrowbysuites.com

Target Market(s)

Men and woman

Industry/Entity Type

Boutique coastal hotel

Contact Information for Business Card

Marrowby Suites Seldovia Alaska marrowby_suites@mailnest.net

Requirements
Must have
• Classy - clever -bold 907-581-6142 call or text

```html
<!DOCTYPE html>
<html lang="en">
<head>
<meta charset="utf-8">
<title>Marrowby Suites – Business Card</title>
<link href="https://fonts.googleapis.com/css2?family=Montserrat:wght@400;500;700;800&display=swap" rel="stylesheet">
<style>
  :root{
    --canvas:#d9d9db;
    --card:#141517;
    --edge:#d8202a;
    --red:#d8202a;
    --yellow:#f3c623;
    --white:#f4f4f4;
    --navy:#2f4b6e;
  }
  *{margin:0;padding:0;box-sizing:border-box}
  html,body{width:1200px;height:800px;overflow:hidden}
  body{
    background:var(--canvas);
    font-family:"Montserrat",Arial,sans-serif;
    display:flex;align-items:center;justify-content:center;gap:40px;
  }
  .card{
    width:540px;height:309px;
    background:var(--card);
    border-radius:22px;
    border-bottom:3px solid var(--edge);
    border-right:2px solid var(--edge);
    position:relative;
    overflow:hidden;
  }
  /* back side */
  .card--back{display:flex;align-items:center;padding:0 30px 0 34px}
  .brand-small{
    width:200px;flex:none;display:flex;align-items:center;gap:8px;
    align-self:flex-end;margin-bottom:96px;
  }
  .brand-small .mark{width:12px;height:12px;background:var(--navy);flex:none}
  .brand-small .name{
    color:var(--navy);font-weight:500;font-size:15px;letter-spacing:1px;
    text-transform:uppercase;white-space:nowrap;
  }
  .details{flex:1;padding-left:14px}
  .person__name{color:var(--yellow);font-weight:800;font-size:21px;letter-spacing:.5px;text-transform:uppercase;white-space:nowrap}
  .person__role{color:var(--red);font-size:13px;margin:2px 0 16px}
  .contact{display:flex;align-items:center;gap:12px;margin-bottom:14px}
  .contact__icon{
    width:30px;height:30px;border-radius:7px;background:var(--red);
    display:flex;align-items:center;justify-content:center;flex:none;
  }
  .contact__text{color:var(--white);font-size:12px;line-height:1.35;white-space:nowrap}
  .contact__label{font-size:14px;font-weight:500;letter-spacing:.5px}
  .contact__phone{font-size:17px;font-weight:800;letter-spacing:.5px}
  /* front side */
  .card--front{display:flex;align-items:center;justify-content:center}
  .brand-large{display:flex;align-items:center;gap:16px}
  .brand-large .mark{width:30px;height:30px;background:var(--red);flex:none}
  .brand-large .name{
    color:var(--white);font-weight:500;font-size:36px;letter-spacing:4px;text-transform:uppercase;white-space:nowrap;
  }
</style>
</head>
<body>
  <section class="card card--back" aria-label="Business card back">
    <div class="brand-small">
      <span class="mark"></span>
      <span class="name">Marrowby Suites</span>
    </div>
    <div class="details">
      <p class="person__name">Daniel Harrow</p>
      <p class="person__role">President</p>
      <div class="contact">
        <span class="contact__icon">
          <svg width="16" height="16" viewBox="0 0 24 24" aria-hidden="true"><path d="M12 2a7 7 0 0 0-7 7c0 5 7 13 7 13s7-8 7-13a7 7 0 0 0-7-7zm0 9.5A2.5 2.5 0 1 1 12 6.5a2.5 2.5 0 0 1 0 5z" fill="#f3c623"/></svg>
        </span>
        <p class="contact__text">418 Brantwell Avenue<br>Kestrel Cove, Alaska 99571</p>
      </div>
      <div class="contact">
        <span class="contact__icon">
          <svg width="16" height="16" viewBox="0 0 24 24" aria-hidden="true"><path d="M6.6 10.8a15 15 0 0 0 6.6 6.6l2.2-2.2a1 1 0 0 1 1-.25 11.4 11.4 0 0 0 3.6.57 1 1 0 0 1 1 1V20a1 1 0 0 1-1 1A17 17 0 0 1 3 4a1 1 0 0 1 1-1h3.5a1 1 0 0 1 1 1c0 1.25.2 2.45.57 3.57a1 1 0 0 1-.25 1z" fill="#f3c623"/></svg>
        </span>
        <p class="contact__text"><span class="contact__label">CALL OR TEXT</span><br><span class="contact__phone">907-581-6142</span></p>
      </div>
      <div class="contact">
        <span class="contact__icon">
          <svg width="16" height="16" viewBox="0 0 24 24" aria-hidden="true"><circle cx="12" cy="12" r="9" fill="none" stroke="#f3c623" stroke-width="2"/><path d="M3 12h18M12 3c3 3 3 15 0 18M12 3c-3 3-3 15 0 18" fill="none" stroke="#f3c623" stroke-width="1.6"/></svg>
        </span>
        <p class="contact__text">marrowby_suites@mailnest.net<br>primemarrowbysuites.com</p>
      </div>
    </div>
  </section>

  <section class="card card--front" aria-label="Business card front">
    <div class="brand-large">
      <span class="mark"></span>
      <span class="name">Marrowby Suites</span>
    </div>
  </section>
</body>
</html>
```